Flyer Design Project for Brightwater Wellbeing Rooms

We are a psychology clinic that specialises in eating, parenting and chronic illness & pain. See our website for a summary.

We need a flyer that will go to doctors and schools in the local area.

Things to include on the front page:

Immediate appointments available
After hours appointments available
Male and female psychologists

Phone 9563 2190
Web brightwaterwellbeingrooms.com.au

On the back page:

Phone 9563 2190
Suite 1/1287 Marlowe Rd, Kelverton East 3185.
brightwaterwellbeingrooms.com.au

Parenting: Parenthood is an amazing journey, but for lots of people it raises all sorts of issues from fear of birth, breastfeeding difficulties and settling problems, to toddler discipline and food fussiness all the way through to getting help for your depressed or anxious adolescent. Our Parenting Psychologists can help you be the best parent you can be which will in turn lead to happier families, homes, children and parents.

Chronic illness/pain: Diabetes, heart disease, arthritis, asthma, migraines, dizziness, chronic fatigue syndrome, infertility, and PCOS are just some of the conditions that can be managed with psychological interventions. Everything we do is about helping you to manage your condition and get back to focusing on what you really want your life to be about.

Eating: Whether you suffer from anorexia, bulimia or binge eating, our strategies help you develop a healthy relationship with food and your body. The practical tips and strategies that we can provide are very useful for people undergoing lapband surgery or liposuction.

I am interested in whether the photographs that I have already purchased can be used...so please have a look through the website and see which you think will suit your design. Photographs are not absolutely necessary though, so if it doesn't fit with your idea that is okay too.
Updates

HI Everyone,

Thanks for submitting so far! I haven't found anything yet that has hit the mark. And I am thinking that is my fault and maybe that way i have described what I want. I apologise and hope that this update might help.

This brochure is likely to sit with lots of other brochures in a doctors waiting room so it needs to be different - so that it will be noticed.

The majority of our market are women - so something feminine is important. Maybe it needs to be a little more playful that I had initially thought. Like maybe not your standard blocky text and bolds and primary colours. But something more creative, more personal.

I want to not focus just on the family theme. Parenting is one area that we cover, but also we help people with eating disorders and chronic illness/chronic pain. So the photographs that I use need to be more general. It is importnat to focus on happy and healthy looking people. As we went to appeal to what my potential clients want to look like and feel like.

I do hope this helps to guide you. I promise that once I see a flyer that I could choose, I will turn the funding to guaranteed. I did this last time...I am just a bit nervous as I haven't received anything yet that I am excited about.

Kindest regards,

Marnie.

Hi Everyone,

Thank you for your designs coming in! As promised, as soon as I received a design that I could see myself choosing I would change the status from refundable to committed. I have now done this!

I have received a design that I would say is good. It is not perfect however...so please keep the ideas coming.

To give more direction, the one that came in has a nice theme that runs through the brochure. Not too many different types of font and colours detracting from the flow of the flyer. However, the thing that I am concerned about is whether it will stand out enough on a rack of other flyers in a doctors waiting room.

I hope this helps with your creative ideas.

Thanks again to everyone!

Marnie.

Thanks SO much to everyone who is putting in designs. You are making my decision difficult!

I am wondering if you can update your designs with a few things:

can I ask you to make some text changes:

1. Can we have a heading on the front page: Psychologists  and then can you put Kelverton East in smaller writing just below it?

2. Id like to say on the front: Specialising in parenting, disordered eating and chronic pain & illness

3. Delete Male & Female Psychologists

4. In general we dont' need to have the logo standing out. We don't have a well known brand yet, so I am not wanting to take up valuable space with this - so perhaps it shoudl be small and maybe just on the back? Keeping the name of our clinic on the front with the website shoudl be sufficient.

Thanks heaps everyone...I will make decision very soon!

Target Market(s)

20-40 year olds. Working. Educated. Female. They might have a family/children.
Australian. Engish speaking.

Industry/Entity Type

Clinic

Requirements
Must have
• I would like to include our logo. Please do not use the colour green that it is in. I hate that colour! but I LOVE the logo.

I would like to follow through with some of the themes of the website and other stationary.

I will attach some of the other stationary I have had designed.

I really like the colours in the letterhead - especially that blue of the logo.

I think it needs to have a dash of colour with it at least...something that will stand out and be noticed on a brochure rack...but also have a look of class/sophistication/modern.
Nice to have
• Perhaps photograph of happy and healthy people.
Should not have
• I don't like bold text or too many different types of fonts.

It shouldn't look too cluttered so I might need to reduce the text I have included - I will need to see it first.

```html
<!DOCTYPE html>
<html lang="en">
<head>
<meta charset="utf-8">
<title>Brightwater Wellbeing Rooms – Flyer</title>
<link rel="stylesheet" href="https://fonts.googleapis.com/css2?family=Open+Sans:wght@300;400;600&display=swap">
<style>
  :root {
    --teal-deep: #0b666c;
    --teal-mid: #138a90;
    --teal-light: #80c5c7;
    --teal-pale: #c6e6e7;
    --teal-text: #136f74;
    --ink-grey: #555a5e;
    --logo-grey: #6b6e70;
    --sky-top: #a9d8ef;
    --sky-low: #e9f3f6;
    --backdrop: #eceeee;
    --white: #ffffff;
    --s1: #6a9e86; --s2: #7fc8cc; --s3: #6fa3a3; --s4: #7b8a96;
    --s5: #3a7a78; --s6: #404244; --s7: #8b8a70;
    --b1: #7fc6c8; --b2: #6fa5a5; --b3: #7b8891;
  }
  * { box-sizing: border-box; margin: 0; padding: 0; }
  html, body { width: 1200px; height: 1169px; overflow: hidden; }
  body { background: var(--backdrop); font-family: "Open Sans", Arial, sans-serif; position: relative; }

  .panel {
    position: absolute; top: 20px; width: 441px; height: 941px;
    background: var(--white); overflow: hidden;
    transform: scale(1.2); transform-origin: 0 0;
  }
  .panel--front { left: 43px; }
  .panel--back { left: 630px; }
  .panel-shapes { position: absolute; inset: 0; width: 441px; height: 941px; }

  .photo-area { position: absolute; left: 0; top: 17px; width: 441px; height: 480px;
    background: linear-gradient(180deg, var(--sky-top) 0%, var(--sky-low) 45%, #f4f1ee 100%); }

  .brand-mini { position: absolute; left: 30px; top: 44px; display: flex; align-items: center; gap: 8px;
    color: var(--white); font-size: 10px; letter-spacing: 2px; text-transform: uppercase; line-height: 1.25; }
  .brand-mini .dot { width: 26px; height: 26px; border-radius: 50%; background: var(--teal-light); flex: none; }

  .headline { position: absolute; left: 10px; top: 418px; color: var(--white);
    font-weight: 300; font-size: 27px; line-height: 32px; }

  .availability { position: absolute; left: 12px; top: 514px; color: var(--white); }
  .availability h2 { font-weight: 400; font-size: 21px; margin-bottom: 10px; }
  .availability ul { list-style: none; }
  .availability li { font-size: 10.5px; font-weight: 600; line-height: 21.5px; text-transform: uppercase; padding-left: 18px; position: relative; }
  .availability li::before { content: ""; position: absolute; left: 1px; top: 7px; width: 5px; height: 5px;
    border-right: 1.5px solid var(--white); border-top: 1.5px solid var(--white); transform: rotate(45deg); }

  .brand { position: absolute; display: flex; align-items: center; gap: 14px;
    color: var(--logo-grey); font-weight: 400; font-size: 16.5px; letter-spacing: 3px; text-transform: uppercase; line-height: 20px; }
  .brand .dot { width: 54px; height: 54px; border-radius: 50%; background: var(--teal-light); flex: none; }
  .panel--front .brand { left: 192px; top: 672px; }
  .panel--back .brand { left: 188px; top: 728px; }

  .contact-web, .contact-phone { position: absolute; right: 16px; color: var(--teal-text); display: flex; align-items: center; gap: 8px; white-space: nowrap; }
  .contact-web { top: 765px; font-size: 13.5px; }
  .contact-phone { top: 793px; font-size: 27px; font-weight: 300; }
  .icon { flex: none; }

  .strip-top { position: absolute; left: 0; top: 0; width: 441px; height: 17px; display: flex; }
  .strip-top span { flex: 1; }
  .strip-bottom { position: absolute; left: 0; bottom: 0; width: 441px; height: 46px; display: flex; }
  .strip-bottom span { flex: 1; }

  .service { position: absolute; left: 19px; width: 403px; color: var(--ink-grey); }
  .service h3 { color: var(--teal-text); font-weight: 400; font-size: 16px; margin-bottom: 3px; }
  .service p { font-size: 10.4px; line-height: 18.6px; text-align: justify; }
  .service--parenting { top: 32px; }
  .service--illness { top: 180px; }
  .service--eating { top: 307px; width: 372px; }
  .service--eating p { text-align: left; }

  .back-web { position: absolute; left: 16px; top: 498px; color: var(--white); font-size: 13px; display: flex; align-items: center; gap: 8px; white-space: nowrap; }
  .back-address { position: absolute; left: 22px; top: 564px; color: var(--white); font-size: 15.5px; line-height: 21px; display: flex; gap: 11px; white-space: nowrap; }
  .back-phone { position: absolute; left: 22px; top: 612px; color: var(--teal-text); font-size: 27px; font-weight: 300; display: flex; align-items: center; gap: 14px; }
</style>
</head>
<body>

<section class="panel panel--front">
  <div class="photo-area" role="img" aria-label="Photograph of a smiling family of four against a bright blue sky"></div>
  <svg class="panel-shapes" viewBox="0 0 441 941" aria-hidden="true">
    <defs>
      <linearGradient id="deepFront" x1="0" y1="0" x2="1" y2="0">
        <stop offset="0" stop-color="var(--teal-mid)"/><stop offset="1" stop-color="var(--teal-deep)"/>
      </linearGradient>
    </defs>
    <polygon points="441,245 296,491 441,491" fill="var(--teal-light)"/>
    <polygon points="441,290 330,491 345,491 441,320" fill="var(--teal-pale)" opacity=".6"/>
    <polygon points="0,378 226,423 296,491 0,491" fill="url(#deepFront)"/>
    <polygon points="296,491 441,491 441,573 316,515" fill="url(#deepFront)"/>
    <polygon points="0,491 296,491 0,873" fill="var(--teal-light)"/>
    <polygon points="296,491 0,873 0,895 310,491" fill="var(--teal-pale)"/>
  </svg>
  <div class="strip-top"><span style="background:var(--s1)"></span><span style="background:var(--s2)"></span><span style="background:var(--s3)"></span><span style="background:var(--s4)"></span><span style="background:var(--s5)"></span><span style="background:var(--s2)"></span><span style="background:var(--s6)"></span><span style="background:var(--s7)"></span></div>

  <div class="brand-mini"><span class="dot"></span><span>Brightwater<br>Wellbeing<br>Rooms</span></div>

  <h1 class="headline">Being the Best<br>Parent you can be</h1>

  <div class="availability">
    <h2>Availability</h2>
    <ul>
      <li>Male and female psychologists</li>
      <li>Immediate appointments</li>
      <li>After hours appointments</li>
    </ul>
  </div>

  <div class="brand"><span class="dot"></span><span>Brightwater<br>Wellbeing<br>Rooms</span></div>

  <div class="contact-web">brightwaterwellbeingrooms.com.au
    <svg class="icon" width="17" height="17" viewBox="0 0 20 20"><circle cx="10" cy="10" r="9" fill="var(--teal-text)"/><path d="M4 7c3 0 4 2 3 4s1 4 0 6M12 2c-1 3 2 4 4 4M13 12c2 0 3 2 2 4" stroke="#fff" stroke-width="1.4" fill="none"/></svg>
  </div>
  <div class="contact-phone">9563 2190
    <svg class="icon" width="12" height="22" viewBox="0 0 12 22"><path d="M3 2h4v5H5v8h2v5H3C1 20 1 2 3 2z" fill="var(--teal-text)"/></svg>
  </div>

  <div class="strip-bottom"><span style="background:var(--b1)"></span><span style="background:var(--b2)"></span><span style="background:var(--b3)"></span></div>
</section>

<section class="panel panel--back">
  <svg class="panel-shapes" viewBox="0 0 441 941" aria-hidden="true">
    <defs>
      <linearGradient id="deepBack" x1="0" y1="0" x2="1" y2="0">
        <stop offset="0" stop-color="var(--teal-mid)"/><stop offset="1" stop-color="var(--teal-deep)"/>
      </linearGradient>
    </defs>
    <polygon points="441,292 318,540 441,540" fill="var(--teal-light)"/>
    <polygon points="441,320 350,540 365,540 441,350" fill="var(--teal-pale)" opacity=".6"/>
    <polygon points="0,425 275,478 318,540 0,540" fill="url(#deepBack)"/>
    <polygon points="318,540 441,540 441,621 337,563" fill="url(#deepBack)"/>
    <polygon points="0,540 318,540 0,873" fill="var(--teal-light)"/>
    <polygon points="318,540 0,873 0,895 332,540" fill="var(--teal-pale)"/>
  </svg>
  <div class="strip-top"><span style="background:var(--s1)"></span><span style="background:var(--s2)"></span><span style="background:var(--s3)"></span><span style="background:var(--s4)"></span><span style="background:var(--s5)"></span><span style="background:var(--s2)"></span><span style="background:var(--s6)"></span><span style="background:var(--s7)"></span></div>

  <article class="service service--parenting">
    <h3>Parenting</h3>
    <p>Parenthood is an amazing journey, but for lots of people it raises all sorts of issues from fear of birth, breastfeeding difficulties and settling problems, to toddler discipline and food fussiness all the way through to getting help for your depressed or anxious adolescent. Our Parenting Psychologists can help you be the best parent you can be which will in turn lead to happier families, homes, children and parents.</p>
  </article>
  <article class="service service--illness">
    <h3>Chronic illness/pain</h3>
    <p>Diabetes, heart disease, arthritis, asthma, migraines, dizziness, chronic fatigue syndrome, infertility, and PCOS are just some of the conditions that can be managed with psychological interventions. Everything we do is about helping you to manage your condition and get back to focusing on what you really want your life to be about.</p>
  </article>
  <article class="service service--eating">
    <h3>Eating</h3>
    <p>Whether you suffer from anorexia, bulimia or binge eating, our strategies help you develop a healthy relationship with food and your body. The practical tips and strategies that we can provide are very useful for people undergoing lapband surgery or liposuction.</p>
  </article>

  <div class="back-web">
    <svg class="icon" width="17" height="17" viewBox="0 0 20 20"><circle cx="10" cy="10" r="9" fill="#fff"/><path d="M4 7c3 0 4 2 3 4s1 4 0 6M12 2c-1 3 2 4 4 4M13 12c2 0 3 2 2 4" stroke="var(--teal-deep)" stroke-width="1.4" fill="none"/></svg>
    brightwaterwellbeingrooms.com.au
  </div>
  <div class="back-address">
    <svg class="icon" width="13" height="19" viewBox="0 0 13 19"><path d="M6.5 0C2.9 0 0 2.9 0 6.5 0 11 6.5 19 6.5 19S13 11 13 6.5C13 2.9 10.1 0 6.5 0z" fill="#fff"/><circle cx="6.5" cy="6.5" r="2.4" fill="var(--teal-light)"/></svg>
    <span>Suite 1/1287 Marlowe Rd,<br>Kelverton East 3185</span>
  </div>
  <div class="back-phone">
    <svg class="icon" width="12" height="22" viewBox="0 0 12 22"><path d="M9 2H5v5h2v8H5v5h4c2 0 2-18 0-18z" fill="#fff"/></svg>
    9563 2190
  </div>

  <div class="brand"><span class="dot"></span><span>Brightwater<br>Wellbeing<br>Rooms</span></div>

  <div class="strip-bottom"><span style="background:var(--b1)"></span><span style="background:var(--b2)"></span><span style="background:var(--b3)"></span></div>
</section>

</body>
</html>
```